Kestrel Plumbing Solutions

This is for my new plumbing company, I have attached an example of what I’m going for but want it to look better.

Target Market(s)

Home owners, real estate, etc.

Industry/Entity Type

Plumbing

• As per my logo and other examples uploaded

Colors

Designer to choose colors to be used in the design.

Requirements
Must have
• Must include my logo provided and similar to my flyer I have attached but better

```html
<!DOCTYPE html>
<html lang="en">
<head>
<meta charset="utf-8">
<title>Kestrel Plumbing Solutions – Flyer</title>
<link href="https://fonts.googleapis.com/css2?family=Montserrat:wght@700;800&family=Roboto:wght@400;500;700&display=swap" rel="stylesheet">
<style>
  :root {
    --navy: #0e3a6b;
    --navy-deep: #0a2d55;
    --blue: #1f7bc8;
    --blue-bright: #2a8ad6;
    --white: #ffffff;
    --ink: #0e3a6b;
    --stage: #123f72;
  }
  * { margin: 0; padding: 0; box-sizing: border-box; }
  html, body { width: 1200px; height: 1200px; overflow: hidden; background: var(--stage); }
  .stage { position: relative; width: 1200px; height: 1200px; }
  .flyer {
    position: absolute; left: 248px; top: 100px;
    width: 594px; height: 850px;
    transform: scale(1.1734); transform-origin: 0 0;
    overflow: hidden; background: var(--navy);
    font-family: "Roboto", Arial, sans-serif; color: var(--ink);
    box-shadow: 0 10px 30px rgba(0,0,0,0.3);
  }
  .flyer-shapes { position: absolute; inset: 0; width: 594px; height: 850px; }
  .abs { position: absolute; white-space: nowrap; }

  .brand-mark { left: 104px; top: 100px; width: 62px; height: 62px; border-radius: 50%; background: var(--white); }
  .brand-name { left: 192px; top: 86px; font-family: "Montserrat", Arial, sans-serif; font-weight: 800; font-size: 40px; color: var(--white); letter-spacing: 0.5px; }
  .brand-sub { left: 206px; top: 146px; font-family: "Montserrat", Arial, sans-serif; font-weight: 700; font-size: 15.5px; color: var(--white); }
  .brand-tagline { left: 172px; top: 172px; font-size: 12px; color: var(--white); letter-spacing: 0.2px; }

  .section-title { left: 40px; top: 370px; font-weight: 700; font-size: 24px; line-height: 34px; color: var(--ink); }

  .service { display: flex; align-items: center; gap: 24px; font-size: 14px; font-weight: 500; color: var(--ink); }
  .service-icon { width: 26px; height: 26px; border-radius: 50%; background: var(--blue); flex: none; display: flex; align-items: center; justify-content: center; }
  .service-icon svg { width: 15px; height: 15px; }
  .service-label.two-line { white-space: normal; line-height: 17px; }

  .feature-title { left: 42px; top: 642px; font-weight: 700; font-size: 26px; color: var(--ink); }
  .feature-lead { left: 46px; top: 690px; font-size: 19px; font-weight: 500; color: var(--ink); }
  .feature-offer { left: 44px; top: 714px; font-family: "Montserrat", Arial, sans-serif; font-weight: 800; font-size: 34px; color: var(--ink); }
  .feature-note { left: 46px; top: 758px; font-size: 17px; font-weight: 500; color: var(--ink); }

  .contact-title { left: 382px; top: 686px; font-weight: 700; font-size: 24px; color: var(--white); }
  .contact-line { left: 382px; top: 746px; font-weight: 700; font-size: 20px; line-height: 30px; color: var(--white); }
</style>
</head>
<body>
<div class="stage">
  <div class="flyer">
    <svg class="flyer-shapes" viewBox="0 0 594 850" aria-hidden="true">
      <defs>
        <linearGradient id="mascotTone" x1="0" y1="0" x2="0" y2="1">
          <stop offset="0" stop-color="#1b5a9c"/>
          <stop offset="1" stop-color="#0e3a6b"/>
        </linearGradient>
      </defs>
      <rect width="594" height="850" fill="var(--navy)"/>
      <polygon points="500,0 594,0 594,410 385,225" fill="var(--blue)"/>
      <polygon points="0,218 385,212 594,400 594,470 0,310" fill="var(--blue)"/>
      <g fill="var(--white)">
        <polygon points="0,250 12,246 0,262"/>
        <polygon points="0,275 32,240 44,240 0,290"/>
        <polygon points="0,305 58,240 70,240 4,316"/>
        <polygon points="20,320 82,245 94,245 32,323"/>
        <polygon points="44,326 104,252 116,252 56,330"/>
        <polygon points="68,332 126,258 138,258 80,336"/>
      </g>
      <polygon points="0,318 594,470 594,480 0,328" fill="var(--navy)"/>
      <polygon points="0,330 594,482 594,850 0,850" fill="var(--white)"/>
      <polygon points="270,725 300,705 340,705 292,850 252,850" fill="var(--blue)"/>
      <polygon points="355,655 594,655 594,850 282,850 318,745 345,728" fill="var(--navy)"/>
    </svg>

    <div class="abs mascot" role="img" aria-label="Mascot illustration of the company character walking" style="left:403px;top:195px;width:160px;height:210px;">
      <svg width="160" height="210" viewBox="0 0 160 210" aria-hidden="true">
        <ellipse cx="80" cy="105" rx="72" ry="100" fill="url(#mascotTone)"/>
      </svg>
    </div>

    <div class="abs brand-mark" aria-hidden="true"></div>
    <div class="abs brand-name">KESTREL</div>
    <div class="abs brand-sub">PLUMBING SOLUTIONS</div>
    <div class="abs brand-tagline">RELIABLE PLUMBING. REAL SOLUTIONS.</div>

    <h2 class="abs section-title">Our Expertise<br>What We Do</h2>

    <div class="abs service" style="left:38px;top:459px;"><span class="service-icon"><svg viewBox="0 0 16 16"><path d="M3 5h10v6H3z" fill="none" stroke="#fff" stroke-width="1.6"/></svg></span><span class="service-label">Emergency Plumbing</span></div>
    <div class="abs service" style="left:38px;top:498px;"><span class="service-icon"><svg viewBox="0 0 16 16"><path d="M3 4h10l-2 9H5z" fill="none" stroke="#fff" stroke-width="1.6"/></svg></span><span class="service-label">Blocked Drains &amp; Sewer</span></div>
    <div class="abs service" style="left:38px;top:537px;"><span class="service-icon"><svg viewBox="0 0 16 16"><path d="M5 2v12M5 8h7" fill="none" stroke="#fff" stroke-width="1.8"/></svg></span><span class="service-label">Gas Fitting &amp; Repairs</span></div>
    <div class="abs service" style="left:38px;top:577px;"><span class="service-icon"><svg viewBox="0 0 16 16"><path d="M3 6h8v4H3zM11 8h3" fill="none" stroke="#fff" stroke-width="1.6"/></svg></span><span class="service-label">Leaking Fixtures</span></div>

    <div class="abs service" style="left:288px;top:459px;"><span class="service-icon"><svg viewBox="0 0 16 16"><rect x="3" y="4" width="10" height="9" fill="none" stroke="#fff" stroke-width="1.6"/></svg></span><span class="service-label">Hot Water Systems</span></div>
    <div class="abs service" style="left:288px;top:496px;"><span class="service-icon"><svg viewBox="0 0 16 16"><circle cx="8" cy="8" r="4" fill="none" stroke="#fff" stroke-width="1.6"/></svg></span><span class="service-label">Pipe Relining &amp; Repairs</span></div>
    <div class="abs service" style="left:288px;top:535px;"><span class="service-icon"><svg viewBox="0 0 16 16"><circle cx="8" cy="8" r="5" fill="none" stroke="#fff" stroke-width="1.4"/><circle cx="8" cy="8" r="2" fill="#fff"/></svg></span><span class="service-label two-line">Camera &amp; Locating<br>Services</span></div>
    <div class="abs service" style="left:288px;top:577px;"><span class="service-icon"><svg viewBox="0 0 16 16"><path d="M3 8l5-5 5 5M4.5 7v6h7V7" fill="none" stroke="#fff" stroke-width="1.6"/></svg></span><span class="service-label">TMV Maintenance</span></div>

    <h2 class="abs feature-title">Feature Highlight</h2>
    <p class="abs feature-lead">Mention this flyer for</p>
    <p class="abs feature-offer">15% OFF</p>
    <p class="abs feature-note">Your first service!</p>

    <h2 class="abs contact-title">Contact</h2>
    <p class="abs contact-line">Book online:<br>kestrelplumbing.com</p>
  </div>
</div>
</body>
</html>
```